Vormet Reserve new label design.

Vormet needs a new image that communicates quality, authenticity and modernity.
Our marketing strategy is based on competitive price and good quality.

We need the design shown below (8 wines):

1. Spanish red wine
2. Spanish red wine
3. French red wine .
4. Chilean red wine .
5. Argentine red wine .
6. Mexican red wine .
7. French red wine.
8. Italian red wine .

One base design with 8 variations and colors ... we what the Caldorino line of wine per say. Or another good example is the Brisk Spring line.
Updates

Justo to clarify an important issue: we need a new LABEL not a new logo. You can find the logo file (vormet logo 2013-grid) on the proyect. Thanks!

Target Market(s)

Premium shoppers from wine want quality and design.

Industry/Entity Type

Marketing

Requirements
Must have
• The new logo *Find it on the files. *
Year of production.
Type of grape.
Country.
Region.
Bottles preferably with the traditional silhouette of 750 ml.
Label size it´s up to you.
Nice to have
• I uploaded some examples of "line products" , this is what we are looking for to have in Vormet Reserve.

```html
<!DOCTYPE html>
<html lang="en">
<head>
<meta charset="utf-8">
<title>Vormet Reserve – Merlot label range</title>
<link href="https://fonts.googleapis.com/css2?family=Bodoni+Moda:wght@400&family=Lato:ital,wght@0,300;1,300&display=swap" rel="stylesheet">
<style>
  :root {
    --page: #ffffff;
    --top-bar: #000000;
    --ink: #ffffff;
    --rule: rgba(255,255,255,0.85);
    --france-bg: #32287f;  --france-fruit: #26215a;
    --chile-bg: #e8501e;   --chile-fruit: #e30613;
    --spain-bg: #be1622;   --spain-fruit: #e30613;
    --mexico-bg: #e5007e;  --mexico-fruit: #a61a5a;
    --italy-bg: #0a6633;   --italy-fruit: #3aaa35;
    --argentina-bg: #009fe3; --argentina-fruit: #ffffff;
  }
  * { margin: 0; padding: 0; box-sizing: border-box; }
  html, body { width: 1200px; height: 1000px; overflow: hidden; background: var(--page); }
  .canvas { position: relative; width: 1200px; height: 1000px; }
  .top-bar { position: absolute; left: 0; top: 0; width: 1200px; height: 8px; background: var(--top-bar); }

  .label {
    position: absolute; width: 219px; height: 357px;
    background: var(--bg); color: var(--ink); overflow: hidden;
  }
  .label--france    { --bg: var(--france-bg);    --fruit: var(--france-fruit);    left: 234px; top: 103px; }
  .label--chile     { --bg: var(--chile-bg);     --fruit: var(--chile-fruit);     left: 491px; top: 103px; }
  .label--spain     { --bg: var(--spain-bg);     --fruit: var(--spain-fruit);     left: 748px; top: 103px; }
  .label--mexico    { --bg: var(--mexico-bg);    --fruit: var(--mexico-fruit);    left: 234px; top: 493px; }
  .label--italy     { --bg: var(--italy-bg);     --fruit: var(--italy-fruit);     left: 491px; top: 493px; }
  .label--argentina { --bg: var(--argentina-bg); --fruit: var(--argentina-fruit); left: 748px; top: 493px; }

  .grape-cluster {
    position: absolute; left: 76px; top: 0; width: 150px; height: 148px;
    background: radial-gradient(ellipse at 55% 50%, var(--fruit) 0%, var(--fruit) 35%, transparent 72%);
    opacity: 0.9;
  }

  .brand-name {
    position: absolute; left: 10px; bottom: 170px;
    writing-mode: vertical-rl; transform: rotate(180deg);
    font-family: "Bodoni Moda", serif; font-weight: 400; font-size: 24px;
    line-height: 1; white-space: nowrap; color: var(--ink);
  }

  .rule { position: absolute; left: 12px; width: 194px; height: 1px; background: var(--rule); }
  .rule--upper { top: 197px; }
  .rule--lower { top: 294px; }

  .grape {
    position: absolute; left: 12px; top: 207px;
    font-family: "Bodoni Moda", serif; font-size: 19px; line-height: 1;
  }
  .dash { position: absolute; left: 13px; top: 232px; font-family: "Lato", sans-serif; font-weight: 300; font-size: 13px; line-height: 1; }
  .country { position: absolute; left: 12px; top: 247px; font-family: "Lato", sans-serif; font-weight: 300; font-size: 15px; line-height: 1; }
  .region { position: absolute; left: 12px; top: 266px; font-family: "Lato", sans-serif; font-weight: 300; font-style: italic; font-size: 15px; line-height: 1; }
  .vintage {
    position: absolute; left: 12px; top: 300px;
    font-family: "Bodoni Moda", serif; font-size: 14px; line-height: 1;
    text-decoration: underline; text-underline-offset: 3px; text-decoration-thickness: 1px;
    font-variant-numeric: oldstyle-nums;
  }
</style>
</head>
<body>
<main class="canvas">
  <div class="top-bar"></div>

  <article class="label label--france">
    <div class="grape-cluster" role="img" aria-label="Stylised grape cluster of round dots"></div>
    <p class="brand-name">Vormet Reserve</p>
    <div class="rule rule--upper"></div>
    <h2 class="grape">Merlot</h2>
    <span class="dash">-</span>
    <p class="country">France</p>
    <p class="region">Bordeaux</p>
    <div class="rule rule--lower"></div>
    <p class="vintage">2011</p>
  </article>

  <article class="label label--chile">
    <div class="grape-cluster" role="img" aria-label="Stylised grape cluster of round dots"></div>
    <p class="brand-name">Vormet Reserve</p>
    <div class="rule rule--upper"></div>
    <h2 class="grape">Merlot</h2>
    <span class="dash">-</span>
    <p class="country">Chile</p>
    <p class="region">Bordeaux</p>
    <div class="rule rule--lower"></div>
    <p class="vintage">2011</p>
  </article>

  <article class="label label--spain">
    <div class="grape-cluster" role="img" aria-label="Stylised grape cluster of round dots"></div>
    <p class="brand-name">Vormet Reserve</p>
    <div class="rule rule--upper"></div>
    <h2 class="grape">Merlot</h2>
    <span class="dash">-</span>
    <p class="country">Spain</p>
    <p class="region">Bordeaux</p>
    <div class="rule rule--lower"></div>
    <p class="vintage">2011</p>
  </article>

  <article class="label label--mexico">
    <div class="grape-cluster" role="img" aria-label="Stylised grape cluster of round dots"></div>
    <p class="brand-name">Vormet Reserve</p>
    <div class="rule rule--upper"></div>
    <h2 class="grape">Merlot</h2>
    <span class="dash">-</span>
    <p class="country">Mexico</p>
    <p class="region">Bordeaux</p>
    <div class="rule rule--lower"></div>
    <p class="vintage">2011</p>
  </article>

  <article class="label label--italy">
    <div class="grape-cluster" role="img" aria-label="Stylised grape cluster of round dots"></div>
    <p class="brand-name">Vormet Reserve</p>
    <div class="rule rule--upper"></div>
    <h2 class="grape">Merlot</h2>
    <span class="dash">-</span>
    <p class="country">Italy</p>
    <p class="region">Bordeaux</p>
    <div class="rule rule--lower"></div>
    <p class="vintage">2011</p>
  </article>

  <article class="label label--argentina">
    <div class="grape-cluster" role="img" aria-label="Stylised grape cluster of round dots"></div>
    <p class="brand-name">Vormet Reserve</p>
    <div class="rule rule--upper"></div>
    <h2 class="grape">Merlot</h2>
    <span class="dash">-</span>
    <p class="country">Argentina</p>
    <p class="region">Bordeaux</p>
    <div class="rule rule--lower"></div>
    <p class="vintage">2011</p>
  </article>
</main>
</body>
</html>
```